v-orn design for startup inpection service

building and pest inspections what i had in mind was v-orn in large print with prepurchase in small print directly under it and the small tm (tradmark) .Within the C I would like an eye but I don't want to take away from the C so maybe the eye would be done in a fine line?I would also like the Building and Pest inspections to be prominent and large .Have no idea of colors but do like black orange and silver

Target Market(s)

home buyers and realestate agents

Industry/Entity Type

Building

Contact Information for Business Card

v-orn prepurchase, Phone 0417382951, fax 02 93147708, email v-orn@mailbay.com.au ,building and pest inspections

Font styles to use
Sans Serif

Requirements
Must have
• bold color
• simple layout
• bold color
• uncluttered layout
Should not have
• contact details the same size as Building and Pest Inspections

```html
<!DOCTYPE html>
<html lang="en">
<head>
<meta charset="utf-8">
<title>V-ORN Pre-Purchase – Business Card</title>
<link href="https://fonts.googleapis.com/css2?family=Open+Sans:wght@400;600;800&family=Tinos&display=swap" rel="stylesheet">
<style>
  :root {
    --page-bg: #ececec;
    --card-white: #ffffff;
    --ink: #111111;
    --orange: #f07d1e;
    --silver: #c8c8ca;
    --peach: #fde7d6;
    --divider: #5b4a78;
  }
  * { margin: 0; padding: 0; box-sizing: border-box; }
  html, body {
    width: 1200px;
    height: 800px;
    overflow: hidden;
    background: var(--page-bg);
  }
  .canvas {
    position: relative;
    width: 1200px;
    height: 800px;
  }
  .card {
    position: absolute;
    left: 75px;
    top: 100px;
    width: 1050px;
    height: 600px;
    background: var(--card-white);
    border-radius: 22px;
    overflow: hidden;
    box-shadow: 0 6px 22px rgba(0,0,0,0.12);
  }
  .card-swooshes {
    position: absolute;
    inset: 0;
  }
  .brand-mark {
    position: absolute;
    left: 110px;
    top: 160px;
    display: flex;
    align-items: center;
    gap: 18px;
  }
  .brand-mark-dot {
    width: 34px;
    height: 34px;
    border-radius: 50%;
    background: var(--orange);
  }
  .brand-mark-name {
    font-family: "Tinos", serif;
    font-size: 72px;
    color: var(--ink);
    line-height: 1;
  }
  .divider {
    position: absolute;
    left: 520px;
    top: 205px;
    width: 2px;
    height: 170px;
    background: var(--divider);
  }
  .wordmark {
    position: absolute;
    left: 548px;
    top: 188px;
    font-family: "Tinos", serif;
    color: var(--ink);
  }
  .wordmark-name {
    font-size: 112px;
    line-height: 0.9;
    letter-spacing: 2px;
  }
  .wordmark-name sup {
    font-family: "Open Sans", sans-serif;
    font-size: 22px;
    font-weight: 600;
    vertical-align: top;
    margin-left: 6px;
  }
  .wordmark-tagline {
    font-size: 26px;
    letter-spacing: 11px;
    margin-top: 6px;
  }
  .contact {
    position: absolute;
    left: 548px;
    top: 340px;
    display: grid;
    grid-template-columns: 80px auto;
    column-gap: 14px;
    row-gap: 2px;
    font-family: "Open Sans", sans-serif;
    font-size: 22px;
    line-height: 1.3;
  }
  .contact-label { color: var(--orange); }
  .contact-value { color: var(--ink); }
  .service-heading {
    position: absolute;
    left: 60px;
    top: 452px;
    font-family: "Open Sans", sans-serif;
    font-weight: 800;
    font-size: 42px;
    letter-spacing: -0.5px;
    color: var(--ink);
    text-transform: uppercase;
  }
  .footer-band {
    position: absolute;
    left: 0;
    right: 0;
    bottom: 0;
    height: 78px;
    background: var(--orange);
    border-top: 6px solid var(--ink);
  }
</style>
</head>
<body>
  <main class="canvas">
    <section class="card">
      <svg class="card-swooshes" viewBox="0 0 1050 600" aria-hidden="true">
        <path d="M 600 -10 C 840 60 1000 300 975 620" fill="none" stroke="var(--peach)" stroke-width="75"/>
        <path d="M 380 -10 C 620 40 770 220 790 620" fill="none" stroke="var(--silver)" stroke-width="40"/>
      </svg>

      <div class="brand-mark">
        <span class="brand-mark-dot"></span>
        <span class="brand-mark-name">V-ORN</span>
      </div>

      <div class="divider"></div>

      <div class="wordmark">
        <div class="wordmark-name">V-ORN<sup>™</sup></div>
        <div class="wordmark-tagline">PRE-PURCHASE</div>
      </div>

      <dl class="contact">
        <dt class="contact-label">Phone:</dt><dd class="contact-value">0417 382 951</dd>
        <dt class="contact-label">Fax:</dt><dd class="contact-value">02 9314 7708</dd>
        <dt class="contact-label">Email:</dt><dd class="contact-value">v-orn@mailbay.com.au</dd>
      </dl>

      <h1 class="service-heading">Building and Pest Inspections</h1>

      <div class="footer-band"></div>
    </section>
  </main>
</body>
</html>
```